Feel the difference Cool Harbor Airconditioning can make for you!

Trying to promote my business to home owners and residential and commercial real estate agents. Want to promote our services and at the same time tell them a little about ourselves.

Air conditioning and electrical company specialising in air conditioning. Areas of service include installation of split systems and ducted units, service and maintenance to all cooling and heating units, emergency breakdown repairs.

Target Market(s)

Home owners and commercial real estate agents

Industry/Entity Type

Air Conditioning

Font styles to use
Sans Serif

```html
<!DOCTYPE html>
<html lang="en">
<head>
<meta charset="utf-8">
<title>Cool Harbor Airconditioning &amp; Electrical Services</title>
<link href="https://fonts.googleapis.com/css2?family=Encode+Sans+Condensed:wght@300;400;500&family=Encode+Sans+Semi+Condensed:wght@400;500&display=swap" rel="stylesheet">
<style>
  :root {
    --navy: #2e3f93;
    --gold: #e5ad1f;
    --gold-bright: #f4e14a;
    --blue: #1c7fc4;
    --blue-deep: #1565ad;
    --blue-light: #a9d3ee;
    --footer: #131c45;
    --white: #ffffff;
    --sand: #e9a93c;
    --sky: #3f69b8;
    --grass: #8cbf3f;
  }
  * { margin: 0; padding: 0; box-sizing: border-box; }
  html, body { width: 858px; height: 1200px; overflow: hidden; background: var(--white); }
  .flyer {
    position: relative;
    width: 858px;
    height: 1200px;
    overflow: hidden;
    font-family: "Encode Sans Condensed", sans-serif;
    background: var(--white);
  }
  .hero { position: absolute; left: 0; top: 0; width: 858px; height: 460px; }
  .hero svg { display: block; }
  .brand {
    position: absolute;
    left: 330px;
    top: 300px;
    display: flex;
    align-items: center;
    gap: 14px;
  }
  .brand-dot {
    width: 58px; height: 58px;
    border-radius: 50%;
    background: var(--blue);
  }
  .brand-name {
    font-family: "Encode Sans Semi Condensed", sans-serif;
    font-weight: 500;
    font-size: 44px;
    line-height: 1;
    color: var(--white);
    letter-spacing: 1px;
  }
  .headline {
    position: absolute;
    left: 0; top: 478px;
    width: 858px;
    text-align: center;
    font-family: "Encode Sans Semi Condensed", sans-serif;
    font-weight: 400;
    font-size: 37px;
    line-height: 46px;
    text-transform: uppercase;
  }
  .headline .line-navy { color: var(--navy); display: block; }
  .headline .line-gold { color: var(--gold); display: block; }
  .intro {
    position: absolute;
    left: 56px; top: 594px;
    width: 450px;
    font-weight: 300;
    font-size: 23px;
    line-height: 32px;
    color: var(--navy);
  }
  .intro .guarantee { color: var(--gold); font-weight: 400; display: block; }
  .service-title {
    position: absolute;
    left: 56px; top: 804px;
    font-weight: 400;
    font-size: 19px;
    letter-spacing: 0.5px;
    color: var(--gold);
    text-transform: uppercase;
  }
  .service-text {
    position: absolute;
    left: 56px; top: 840px;
    width: 450px;
    font-weight: 300;
    font-size: 23px;
    line-height: 32px;
    color: var(--navy);
  }
  .about {
    position: absolute;
    left: 524px; top: 602px;
    width: 302px; height: 424px;
    border-radius: 34px;
    background: linear-gradient(180deg, var(--blue-deep) 0%, var(--blue) 18%, var(--blue-light) 62%, var(--blue) 86%, var(--blue-deep) 100%);
    color: var(--white);
  }
  .about-title {
    position: absolute;
    left: 58px; top: 16px;
    font-size: 26px;
    font-weight: 400;
    color: var(--gold);
    text-transform: uppercase;
  }
  .about-list {
    position: absolute;
    left: 22px; top: 58px;
    width: 270px;
    list-style: none;
    font-weight: 400;
    font-size: 19.5px;
    line-height: 24px;
  }
  .about-list li { position: relative; padding-left: 36px; }
  .about-list li svg { position: absolute; left: 2px; top: 5px; }
  .call {
    position: absolute;
    left: 0; top: 318px;
    width: 302px;
    text-align: center;
    color: var(--gold-bright);
  }
  .call-label { display: block; font-size: 41px; line-height: 44px; font-weight: 400; padding-left: 36px; }
  .call-number { display: inline-flex; align-items: center; gap: 10px; font-size: 35px; line-height: 42px; font-weight: 400; }
  .footer {
    position: absolute;
    left: 0; top: 1102px;
    width: 858px; height: 98px;
    background: var(--footer);
    text-align: center;
    color: var(--gold-bright);
  }
  .footer-address { display: block; padding-top: 14px; font-size: 24px; line-height: 28px; font-weight: 400; }
  .footer-web { display: block; font-size: 33px; line-height: 44px; font-weight: 400; letter-spacing: 0.5px; }
</style>
</head>
<body>
<div class="flyer">
  <div class="hero">
    <svg width="858" height="460" viewBox="0 0 858 460" role="img" aria-label="Photo of a wall-mounted split system air conditioner above a scene that shifts from hot desert on the left to a green lawn, blue sky and a house on the right">
      <defs>
        <linearGradient id="scene" x1="0" y1="0" x2="1" y2="0">
          <stop offset="0" stop-color="#f2c45a"/>
          <stop offset="0.32" stop-color="#e9a93c"/>
          <stop offset="0.55" stop-color="#9fb8d8"/>
          <stop offset="1" stop-color="#3f69b8"/>
        </linearGradient>
        <linearGradient id="ground" x1="0" y1="0" x2="1" y2="0">
          <stop offset="0" stop-color="#e3b36a" stop-opacity="0.9"/>
          <stop offset="0.45" stop-color="#d9c27a" stop-opacity="0.6"/>
          <stop offset="0.7" stop-color="#8cbf3f" stop-opacity="0.85"/>
          <stop offset="1" stop-color="#7fb33a" stop-opacity="0.9"/>
        </linearGradient>
      </defs>
      <rect x="0" y="0" width="858" height="460" fill="url(#scene)"/>
      <rect x="0" y="250" width="858" height="210" fill="url(#ground)"/>
      <path d="M0,345 Q380,470 858,365 L858,460 L0,460 Z" fill="var(--blue)"/>
      <path d="M0,400 Q400,490 858,378 L858,460 L0,460 Z" fill="var(--white)"/>
    </svg>
  </div>

  <div class="brand">
    <span class="brand-dot"></span>
    <span class="brand-name">COOL HARBOR</span>
  </div>

  <h1 class="headline">
    <span class="line-navy">Why choose Cool Harbor as your</span>
    <span class="line-gold">Airconditioning &amp; Electrical Specialist?</span>
  </h1>

  <p class="intro">
    Fully licensed in both the air conditioning and electrical industries &amp; over 10 years experience! We pride ourselves in our quality of work, neatness and tidiness of the job, and our overall professional attitude
    <span class="guarantee">100% satisfaction guaranteed</span>
  </p>

  <h2 class="service-title">Outstanding customer service</h2>
  <p class="service-text">
    At Cool Harbor we know a well maintained air conditioning system makes all the difference, our professional team of air conditioning mechanics are equipped to carry out all necessary repairs, service and maintenance on all cooling and heating systems.
  </p>

  <aside class="about">
    <h2 class="about-title">About us</h2>
    <ul class="about-list">
      <li><svg width="24" height="18" viewBox="0 0 24 18"><path d="M2,10 L9,16 L22,2" fill="none" stroke="var(--gold)" stroke-width="3.5" stroke-linecap="round" stroke-linejoin="round"/></svg>Quality Work, gauranteed</li>
      <li><svg width="24" height="18" viewBox="0 0 24 18"><path d="M2,10 L9,16 L22,2" fill="none" stroke="var(--gold)" stroke-width="3.5" stroke-linecap="round" stroke-linejoin="round"/></svg>Clean, polite, professional</li>
      <li><svg width="24" height="18" viewBox="0 0 24 18"><path d="M2,10 L9,16 L22,2" fill="none" stroke="var(--gold)" stroke-width="3.5" stroke-linecap="round" stroke-linejoin="round"/></svg>Full trade licenses in air conditioning and electrical</li>
      <li><svg width="24" height="18" viewBox="0 0 24 18"><path d="M2,10 L9,16 L22,2" fill="none" stroke="var(--gold)" stroke-width="3.5" stroke-linecap="round" stroke-linejoin="round"/></svg>Insured</li>
      <li><svg width="24" height="18" viewBox="0 0 24 18"><path d="M2,10 L9,16 L22,2" fill="none" stroke="var(--gold)" stroke-width="3.5" stroke-linecap="round" stroke-linejoin="round"/></svg>On time, all the time</li>
      <li><svg width="24" height="18" viewBox="0 0 24 18"><path d="M2,10 L9,16 L22,2" fill="none" stroke="var(--gold)" stroke-width="3.5" stroke-linecap="round" stroke-linejoin="round"/></svg>Friendly, honest.</li>
      <li><svg width="24" height="18" viewBox="0 0 24 18"><path d="M2,10 L9,16 L22,2" fill="none" stroke="var(--gold)" stroke-width="3.5" stroke-linecap="round" stroke-linejoin="round"/></svg>Our pride and reputation are derived from the satisfaction of our clients.</li>
    </ul>
    <div class="call">
      <span class="call-label">CALL NOW</span>
      <span class="call-number">
        <svg width="26" height="34" viewBox="0 0 26 34" aria-hidden="true"><path d="M7,2 L11,9 L8,12 Q9,19 14,24 L17,21 L24,26 L21,31 Q16,34 10,27 Q3,19 2,10 Q2,4 7,2 Z" fill="var(--gold-bright)"/></svg>
        1300 555 019
      </span>
    </div>
  </aside>

  <footer class="footer">
    <span class="footer-address">Suite 12, 40 Harbour Lane, Melbourne, VIC, 3000</span>
    <span class="footer-web">www.coolharbor.com.au</span>
  </footer>
</div>
</body>
</html>
```